Photoshop Design Project

Just looking to use some existing element in emails and printed flyers for a lunch menu promo.

I am attaching a menu in progress to reference only the front page design of a chalkboard, chalk fonts, tagline of :Trade the Same Old Plate for Midday Fresh Bites. Its on the front of the menu.

I just want to drop in a photo of each on three separate pieces with description.

THe design should not be a match to the front of the menu, just utilize its elements. the design is not a lead at all, these should remain familiar with the front of the menu, but please use the elements to your design preference.

Ok to submit one layout that we can repeat, or ok to submit three different versions

Must stick with the colors though, they are brand color combo, not exact by color code, but the oranges and the browns need to stay somewhere and in some capacity.
SO menu attached, check out the front cover for inspirations, to go in email sends embedded, and to print as a flyer.

There are also three images attached they are the to be dropped into each piece, with a desciption
Updates

Reason: seems to be too many questions and I wasnt getting anywhere.. To clarify...One Design Piece (one page), three separate items, same peice, however three total. one for each product photo supplied

I moved the deadline back as there were many questions. To clarify, one design piece to be reused for three different products (sandwiches in this case) Same piece, but one for each sandwich.

I posted a file called Artsquare that now has each photo partnered with its title and description

Target Market(s)

hungry people looking for lunch

Industry/Entity Type

Promo

Requirements
Must have
• Attached Menu front page elements, of chalkboard, chalk font existing front colors.

```html
<!DOCTYPE html>
<html lang="en">
<head>
<meta charset="utf-8">
<title>Lunch Menu Promo Cards</title>
<link rel="stylesheet" href="https://fonts.googleapis.com/css2?family=Architects+Daughter&display=swap">
<style>
  :root {
    --stage: #1c1c1c;
    --card-frame: #ffffff;
    --brand-orange: #f07f2e;
    --chalk-orange: #ee8a3c;
    --chalkboard: #2e2d2b;
    --chalkboard-edge: #262523;
    --chalk-white: #f2f0ea;
  }
  * { box-sizing: border-box; margin: 0; padding: 0; }
  html, body { width: 1200px; height: 900px; overflow: hidden; }
  body {
    background: var(--stage);
    font-family: "Architects Daughter", cursive;
    position: relative;
  }
  .promo-card {
    position: absolute;
    top: 249px;
    width: 357px;
    height: 416px;
    background: var(--card-frame);
    padding: 13px;
    display: flex;
    flex-direction: column;
  }
  .promo-card--chicken { left: 30px; }
  .promo-card--roast-beef { left: 427px; }
  .promo-card--steak { left: 816px; }
  .sandwich-photo { height: 225px; }
  .sandwich-photo--chicken { background: linear-gradient(135deg, #d9b76a 0%, #5f7a3a 45%, #6b3a20 75%, #c8402c 100%); }
  .sandwich-photo--roast-beef { background: linear-gradient(180deg, #e8c56a 0%, #d39a45 35%, #e8e2c8 55%, #9a6a5e 75%, #d8a45a 100%); }
  .sandwich-photo--steak { background: linear-gradient(180deg, #e6c48e 0%, #d8b27c 35%, #a6544a 60%, #7a3a30 85%, #5c6a34 100%); }
  .orange-band { height: 24px; background: var(--brand-orange); }
  .chalk-panel {
    flex: 1;
    background: radial-gradient(ellipse at center, var(--chalkboard) 60%, var(--chalkboard-edge) 100%);
    text-align: center;
    padding: 8px 14px 0;
    display: flex;
    flex-direction: column;
    align-items: center;
  }
  .item-title {
    color: var(--chalk-white);
    font-size: 14.5px;
    font-weight: 400;
    letter-spacing: 1.4px;
    line-height: 18px;
    text-transform: uppercase;
  }
  .chalk-flourish { width: 300px; height: 28px; margin: 2px 0 6px; }
  .chalk-flourish path { fill: none; stroke: var(--chalk-orange); stroke-width: 2.4; stroke-linecap: round; stroke-linejoin: round; }
  .item-description {
    color: var(--chalk-orange);
    font-size: 10.5px;
    letter-spacing: 0.9px;
    line-height: 13px;
    text-transform: uppercase;
  }
</style>
</head>
<body>
  <article class="promo-card promo-card--chicken">
    <div class="sandwich-photo sandwich-photo--chicken" role="img" aria-label="Photo of grilled BBQ chicken sandwich on focaccia with greens and red pepper"></div>
    <div class="orange-band"></div>
    <div class="chalk-panel">
      <h2 class="item-title" style="margin-top:6px">Bistro BBQ Chicken Sandwich</h2>
      <svg class="chalk-flourish" viewBox="0 0 300 28"><path d="M10 24 L290 8 L170 16 L200 22 L120 24 L10 24"/></svg>
      <p class="item-description">Perfectly grilled BBQ chicken breast,<br>dill yogurt dressing, garlic spread,<br>micro greens, radish, &amp; red bell pepper<br>on fresh focaccia bread</p>
    </div>
  </article>

  <article class="promo-card promo-card--roast-beef">
    <div class="sandwich-photo sandwich-photo--roast-beef" role="img" aria-label="Photo of roast beef sandwich with sprouts on a ciabatta roll"></div>
    <div class="orange-band"></div>
    <div class="chalk-panel">
      <h2 class="item-title">Spicy Roast Beef Sandwich<br>with Danish Smelly Cheese</h2>
      <svg class="chalk-flourish" viewBox="0 0 300 28"><path d="M10 24 L290 8 L170 16 L200 22 L120 24 L10 24"/></svg>
      <p class="item-description">Sprouts, fresh basil, onions &amp; chili sauce<br>on a fresh ciabatta roll</p>
    </div>
  </article>

  <article class="promo-card promo-card--steak">
    <div class="sandwich-photo sandwich-photo--steak" role="img" aria-label="Photo of sliced steak sandwich on ciabatta with watercress"></div>
    <div class="orange-band"></div>
    <div class="chalk-panel">
      <h2 class="item-title">Steak Sandwich with Blue Cheese,<br>Roasted Garlic Mayonnaise &amp;<br>Balsamic Vinegar Reduction</h2>
      <svg class="chalk-flourish" viewBox="0 0 300 28"><path d="M10 18 L290 4 L170 12 L200 18 L120 20 L10 18"/></svg>
      <p class="item-description">Topped with Roquefort cheese &amp;<br>watercress on fresh ciabatta bread</p>
    </div>
  </article>
</body>
</html>
```